Med Spa business card design with logo

Need a logo design and business card for our new company Velora Skinworks Med Spa. We are a medical office that deals with high end clients. We offer them skin care products which include NERVAX, lip augmentation, and various laser for the skin. I king of like the logo attached, maybe something along those lines but also open to any logo concept.
Updates

Target Market(s)

Out target audience are male and females in the age range of 21-80 years of age

Industry/Entity Type

Medical

Contact Information for Business Card

woukd like front of card to have logo and business name VELORA SKINWORKS MEDSPA. Back of card employee name and phone number along with instagram logo and user name

Font styles to use
Serif
Sans Serif

Requirements
Must have
• prefer monochromatic look white, black, gold
Should not have
• not too colorful

```html
<!DOCTYPE html>
<html lang="en">
<head>
<meta charset="utf-8">
<title>Velora Skinworks Med Spa – Business Card</title>
<link href="https://fonts.googleapis.com/css2?family=Lato:wght@400;700&family=Quicksand:wght@300;400&display=swap" rel="stylesheet">
<style>
  :root {
    --stage: #161616;
    --card-light: #ffffff;
    --card-dark: #231f20;
    --ink: #1d1d1d;
    --gold: #c9a04a;
    --gold-light: #e9cd7c;
    --white: #ffffff;
  }
  * { margin: 0; padding: 0; box-sizing: border-box; }
  html, body { width: 1200px; height: 741px; overflow: hidden; }
  body { background: var(--stage); font-family: 'Lato', sans-serif; position: relative; }

  .card {
    position: absolute; top: 229px; width: 495px; height: 282px;
    border-radius: 12px; overflow: hidden;
  }
  .card--front { left: 100px; background: var(--card-light); color: var(--ink); }
  .card--back { left: 607px; background: var(--card-dark); color: var(--white); }

  /* front */
  .edge-dot {
    position: absolute; left: -17px; top: 30px; width: 34px; height: 34px;
    border-radius: 50%; background: linear-gradient(135deg, var(--gold-light), var(--gold));
  }
  .person { position: absolute; left: 30px; top: 33px; }
  .person__name { font-size: 17px; font-weight: 400; letter-spacing: 0.3px; line-height: 19px; }
  .person__role { font-size: 13px; line-height: 14px; }
  .address { position: absolute; left: 30px; top: 130px; font-size: 13px; line-height: 17px; }
  .contacts { position: absolute; left: 30px; top: 187px; list-style: none; font-size: 13px; line-height: 17px; }
  .contacts li { display: flex; align-items: center; gap: 4px; }
  .contacts svg { width: 12px; height: 12px; flex: none; }

  .brand-block {
    position: absolute; right: 22px; top: 70px; width: 190px; height: 150px;
    display: flex; flex-direction: column; align-items: center; justify-content: center; gap: 10px;
  }
  .brand-block__circle { width: 46px; height: 46px; border-radius: 50%; border: 3px solid var(--gold); }
  .brand-block__name {
    font-family: 'Quicksand', sans-serif; font-weight: 400; color: var(--gold);
    font-size: 22px; line-height: 26px; text-align: center;
  }

  /* back */
  .badge {
    position: absolute; left: 204px; top: 48px; width: 82px; height: 82px;
    border-radius: 50%; background: #0f0f0f; border: 2px solid var(--gold);
  }
  .wordmark {
    position: absolute; left: 0; top: 136px; width: 100%; text-align: center;
    font-family: 'Quicksand', sans-serif; font-weight: 300; color: var(--white);
  }
  .wordmark__main { display: block; font-size: 33px; line-height: 36px; }
  .wordmark__sub {
    display: flex; align-items: center; justify-content: center; gap: 12px;
    font-size: 23px; line-height: 26px;
  }
  .wordmark__rule { width: 64px; height: 1px; background: var(--white); }
  .web {
    position: absolute; left: 0; top: 222px; width: 100%; text-align: center;
    font-size: 12.5px; color: var(--white);
  }
  .web__accent { color: var(--gold-light); }
</style>
</head>
<body>

<section class="card card--front">
  <span class="edge-dot"></span>
  <div class="person">
    <p class="person__name">ELENA MARSH</p>
    <p class="person__role">Director</p>
  </div>
  <address class="address" style="font-style:normal">
    PO BOX 48 Harbor Lane<br>7th street Denver ,USA
  </address>
  <ul class="contacts">
    <li><svg viewBox="0 0 12 12"><rect width="12" height="12" rx="2" fill="#c9a04a"/><path d="M3 4h6v4H3z" fill="#fff"/></svg>(01) 5550 1234</li>
    <li><svg viewBox="0 0 12 12"><rect width="12" height="12" rx="2" fill="#c9a04a"/><path d="M3 3h6v6H3z" fill="#fff"/></svg>(01) 5550 1234</li>
    <li><svg viewBox="0 0 12 12"><rect width="12" height="12" rx="2" fill="#c9a04a"/><path d="M2.5 4h7v5h-7zM2.5 4l3.5 3 3.5-3" fill="none" stroke="#fff" stroke-width="1"/></svg>info@veloraskin.com</li>
    <li><svg viewBox="0 0 12 12"><rect width="12" height="12" rx="2" fill="#c9a04a"/><circle cx="6" cy="6" r="3.2" fill="none" stroke="#fff" stroke-width="1"/><path d="M2.8 6h6.4M6 2.8v6.4" stroke="#fff" stroke-width="0.8"/></svg>www.veloraskin.com</li>
  </ul>
  <div class="brand-block">
    <span class="brand-block__circle"></span>
    <p class="brand-block__name">Velora Skinworks<br>Med Spa</p>
  </div>
</section>

<section class="card card--back">
  <span class="badge"></span>
  <h1 class="wordmark">
    <span class="wordmark__main">Velora Skinworks</span>
    <span class="wordmark__sub"><span class="wordmark__rule"></span>Med Spa<span class="wordmark__rule"></span></span>
  </h1>
  <p class="web">www.<span class="web__accent">veloraskin</span>.com</p>
</section>

</body>
</html>
```